Torvaline business cards

Need fresh design for our business cards. Logo must be specific, we are open for everything else.

Contact Information for Business Card

phrase "GMP & JANITORIAL SERVICES" should be used as main point of card

Colors
3176b5
3276b5
85acd3
cedeed
ffffff
0292cd
33a6d7
85cae6
cee9f5

Requirements
Must have
• The logo
Should not have
• crowded designs

```html
<!DOCTYPE html>
<html lang="en">
<head>
<meta charset="utf-8">
<title>Torvaline business cards</title>
<link href="https://fonts.googleapis.com/css2?family=Questrial&display=swap" rel="stylesheet">
<style>
  :root {
    --brand-blue: #3176b5;
    --bright-blue: #1a82c8;
    --ink: #2b2b2b;
    --card-black: #111214;
    --paper: #ffffff;
    --backdrop: #2a2b2d;
  }
  * { margin: 0; padding: 0; box-sizing: border-box; }
  html, body { width: 1200px; height: 852px; overflow: hidden; }
  body {
    background: var(--backdrop);
    font-family: "Questrial", "Century Gothic", sans-serif;
    position: relative;
  }
  .card {
    position: absolute;
    width: 540px;
    height: 308px;
    border-radius: 18px;
    overflow: hidden;
  }
  .card-back { left: 70px; top: 110px; background: var(--card-black); }
  .card-front { left: 590px; top: 434px; background: var(--paper); }

  .brand { position: absolute; display: flex; flex-direction: column; }
  .wordmark {
    display: flex; align-items: center; gap: 12px;
    color: var(--bright-blue);
    letter-spacing: 0.12em;
    line-height: 1;
  }
  .wordmark-dot {
    width: 0.5em; height: 0.5em; border-radius: 50%;
    background: var(--bright-blue);
  }
  .tagline {
    color: var(--bright-blue);
    letter-spacing: 0.28em;
    line-height: 1;
    white-space: nowrap;
  }

  .card-back .brand { left: 0; right: 0; top: 96px; align-items: center; }
  .card-back .wordmark { font-size: 52px; }
  .card-back .tagline { font-size: 13px; margin-top: 12px; }
  .card-back .web {
    position: absolute; left: 0; right: 0; top: 222px;
    text-align: center; color: #ffffff;
    font-size: 15px; letter-spacing: 0.3em;
  }

  .card-front .brand { right: 40px; top: 32px; align-items: flex-end; }
  .card-front .wordmark { font-size: 30px; }
  .card-front .tagline { font-size: 9px; margin-top: 7px; letter-spacing: 0.24em; }

  .rule { position: absolute; height: 1.5px; background: var(--bright-blue); }
  .rule-top { left: 150px; right: 40px; top: 92px; }
  .rule-name { left: 60px; width: 230px; top: 196px; }
  .edge-tab {
    position: absolute; left: 0; top: 160px; width: 12px; height: 38px;
    background: var(--bright-blue);
  }
  .person { position: absolute; left: 60px; top: 150px; }
  .person-name { color: var(--bright-blue); font-size: 18px; letter-spacing: 0.02em; }
  .person-role { color: var(--ink); font-size: 15px; margin-top: 2px; }
  .contacts {
    position: absolute; left: 60px; top: 206px;
    list-style: none; color: var(--ink); font-size: 14px;
  }
  .contacts li { display: flex; align-items: center; gap: 8px; height: 19px; }
  .contacts svg { width: 11px; height: 11px; fill: var(--bright-blue); }
  .address {
    position: absolute; right: 40px; top: 116px;
    text-align: right; color: var(--ink); font-size: 14px; line-height: 1.35;
  }
  .swoosh { position: absolute; left: 0; top: 0; width: 540px; height: 308px; }
</style>
</head>
<body>

<section class="card card-back">
  <div class="brand">
    <div class="wordmark"><span class="wordmark-dot"></span>TORVALINE</div>
    <p class="tagline">GMP &amp; JANITORIAL SERVICES</p>
  </div>
  <p class="web">WWW.TORVALINE.COM</p>
</section>

<section class="card card-front">
  <svg class="swoosh" viewBox="0 0 540 308" aria-hidden="true">
    <path d="M0,296 L360,296 Q386,296 402,274 Q418,252 450,244 L540,220 L540,308 L0,308 Z" fill="var(--bright-blue)"/>
    <path d="M0,285 L352,285 Q374,285 388,266 Q398,254 410,248" fill="none" stroke="var(--bright-blue)" stroke-width="4"/>
  </svg>

  <div class="brand">
    <div class="wordmark"><span class="wordmark-dot"></span>TORVALINE</div>
    <p class="tagline">GMP &amp; JANITORIAL SERVICES</p>
  </div>
  <div class="rule rule-top"></div>

  <div class="address">1187 Marrow Creek Lane<br>Dunmore, OR 97408</div>

  <div class="edge-tab"></div>
  <div class="person">
    <p class="person-name">ALDEN MERCER</p>
    <p class="person-role">Director</p>
  </div>
  <div class="rule rule-name"></div>

  <ul class="contacts">
    <li>
      <svg viewBox="0 0 24 24"><path d="M6.6 10.8a15.1 15.1 0 0 0 6.6 6.6l2.2-2.2a1 1 0 0 1 1-.25 11.4 11.4 0 0 0 3.6.57 1 1 0 0 1 1 1V20a1 1 0 0 1-1 1A17 17 0 0 1 3 4a1 1 0 0 1 1-1h3.5a1 1 0 0 1 1 1c0 1.25.2 2.45.57 3.57a1 1 0 0 1-.25 1z"/></svg>
      (541) 382-0617
    </li>
    <li>
      <svg viewBox="0 0 24 24"><path d="M2 5h20v14H2z M4 7v.4l8 5.2 8-5.2V7z" fill-rule="evenodd"/></svg>
      info@torvaline.com
    </li>
    <li>
      <svg viewBox="0 0 24 24"><circle cx="12" cy="12" r="10"/></svg>
      www.torvaline.com
    </li>
  </ul>
</section>

</body>
</html>
```